Vault 9 Nook Storage Poster Ad

Vault 9 Nook Storage needs an 8.5" X 11" specialty storage products poster.

Graphics that illustrate seasonal tire storage, bicycle storage, and motorcycle storage.

Information on the poster will be as follows:

Tire storage: $99.00/season + tax
bicycle storage: $99.00/season + tax
motorcycle storage: $250.00/season + tax
Phone: 306-555-0148
Web: www.vault9nook.ca
Address: Vault 9 Nook Storage, 4718 Brindle Avenue, Saskatoon, SK, S4M 2J6

**Information does not need to be presented in this exact format. The designer can creatively list the services and the prices. The words phone, web, and address can be left out**

**The season that the ad is targeting is winter

Industry/Entity Type

Storage

```html
<!DOCTYPE html>
<html lang="en">
<head>
<meta charset="utf-8">
<title>Vault 9 Nook Storage – Winter Seasonal Storage</title>
<link rel="stylesheet" href="https://fonts.googleapis.com/css2?family=Arimo:wght@400;700&display=swap">
<style>
  :root {
    --white: #ffffff;
    --ink: #111111;
    --brand-red: #d42a2a;
    --lime: #8dc540;
    --moss: #6a9a42;
    --sun: #fbd04a;
    --amber: #f4ae24;
    --tangerine: #e48127;
    --scarlet: #e0393a;
    --crimson: #bf1a2f;
    --maroon: #8b0b1b;
  }
  * { box-sizing: border-box; margin: 0; padding: 0; }
  html, body { width: 920px; height: 1200px; overflow: hidden; background: var(--white); }
  body { font-family: "Arimo", Arial, sans-serif; }
  .poster { position: relative; width: 920px; height: 1200px; }
  .tile {
    position: absolute;
    display: flex; flex-direction: column; align-items: center;
    text-align: center; font-size: 19px; line-height: 1.35;
  }
  .tile svg { display: block; }
  .tile__label { position: absolute; left: 0; right: 0; }

  .brand { left: 0; top: 0; width: 613px; height: 600px; background: var(--white); justify-content: center; }
  .brand__name { display: flex; align-items: center; gap: 22px; }
  .brand__square { width: 58px; height: 58px; background: var(--brand-red); }
  .brand__text { font-weight: 700; font-size: 62px; line-height: 1.05; color: var(--ink); text-align: left; letter-spacing: 1px; }

  .season { left: 613px; top: 0; width: 307px; height: 300px; background: var(--lime); color: var(--ink); }
  .products { left: 613px; top: 300px; width: 307px; height: 300px; background: var(--moss); color: var(--white); }
  .scooter { left: 0; top: 600px; width: 307px; height: 300px; background: var(--sun); color: var(--ink); }
  .tires { left: 307px; top: 600px; width: 306px; height: 300px; background: var(--amber); color: var(--ink); }
  .bicycle { left: 613px; top: 600px; width: 307px; height: 300px; background: var(--tangerine); color: var(--ink); }
  .phone { left: 0; top: 900px; width: 307px; height: 300px; background: var(--scarlet); color: var(--white); }
  .address { left: 307px; top: 900px; width: 306px; height: 300px; background: var(--crimson); color: var(--white); }
  .web { left: 613px; top: 900px; width: 307px; height: 300px; background: var(--maroon); color: var(--white); }

  .season svg { margin-top: 96px; }
  .season .tile__label { top: 254px; }
  .products svg { margin-top: 83px; }
  .products .tile__label { top: 244px; font-size: 20px; }
  .price svg { margin-top: 90px; }
  .price .tile__label { top: 244px; font-size: 17px; }
  .contact svg { margin-top: 80px; }
  .contact .tile__label { top: 244px; font-size: 17px; }
  .address .tile__label { top: 222px; }
</style>
</head>
<body>
<main class="poster">

  <section class="tile brand">
    <div class="brand__name">
      <span class="brand__square" aria-hidden="true"></span>
      <h1 class="brand__text">Vault 9 Nook<br>Storage</h1>
    </div>
  </section>

  <section class="tile season">
    <svg width="120" height="120" viewBox="-60 -60 120 120" aria-hidden="true">
      <g stroke="#111" stroke-width="9" stroke-linecap="round" fill="none">
        <g id="flake-arm">
          <line x1="0" y1="0" x2="0" y2="-54"/>
          <polyline points="-14,-46 0,-34 14,-46"/>
          <polyline points="-12,-28 0,-18 12,-28"/>
        </g>
        <use href="#flake-arm" transform="rotate(45)"/>
        <use href="#flake-arm" transform="rotate(90)"/>
        <use href="#flake-arm" transform="rotate(135)"/>
        <use href="#flake-arm" transform="rotate(180)"/>
        <use href="#flake-arm" transform="rotate(225)"/>
        <use href="#flake-arm" transform="rotate(270)"/>
        <use href="#flake-arm" transform="rotate(315)"/>
      </g>
    </svg>
    <p class="tile__label">Winter</p>
  </section>

  <section class="tile products">
    <svg width="126" height="126" viewBox="0 0 126 126" aria-hidden="true">
      <g fill="none" stroke="#fff" stroke-width="8" stroke-linejoin="round">
        <polygon points="63,8 118,30 63,52 8,30"/>
        <polygon points="8,30 63,52 63,118 8,94"/>
        <polygon points="118,30 63,52 63,118 118,94"/>
      </g>
      <polygon points="32,18 88,40 98,36 42,14" fill="#fff"/>
      <rect x="84" y="62" width="22" height="8" fill="#fff" transform="skewY(-22) translate(0,34)"/>
    </svg>
    <p class="tile__label">Seasonal storage products</p>
  </section>

  <section class="tile price scooter">
    <svg width="160" height="120" viewBox="0 0 160 120" aria-hidden="true">
      <g fill="#111">
        <circle cx="32" cy="94" r="20"/>
        <circle cx="130" cy="94" r="20"/>
        <path d="M10 88 C10 62 32 54 58 56 L96 56 C104 56 106 50 104 40 L98 16 L108 14 L118 52 C130 60 150 68 152 88 Z"/>
        <rect x="26" y="42" width="40" height="12" rx="6"/>
        <rect x="94" y="6" width="26" height="8" rx="4"/>
      </g>
      <circle cx="32" cy="94" r="7" fill="var(--sun)"/>
      <circle cx="130" cy="94" r="7" fill="var(--sun)"/>
    </svg>
    <p class="tile__label">$250.00/season + tax</p>
  </section>

  <section class="tile price tires">
    <svg width="110" height="130" viewBox="0 0 110 130" aria-hidden="true">
      <ellipse cx="55" cy="65" rx="50" ry="62" fill="#111"/>
      <ellipse cx="55" cy="65" rx="24" ry="36" fill="var(--amber)"/>
      <ellipse cx="55" cy="65" rx="14" ry="24" fill="#111"/>
      <g stroke="var(--amber)" stroke-width="4">
        <line x1="10" y1="40" x2="28" y2="44"/>
        <line x1="6" y1="65" x2="26" y2="65"/>
        <line x1="10" y1="90" x2="28" y2="86"/>
        <line x1="100" y1="40" x2="82" y2="44"/>
        <line x1="104" y1="65" x2="84" y2="65"/>
        <line x1="100" y1="90" x2="82" y2="86"/>
      </g>
    </svg>
    <p class="tile__label">$99.00/season + tax</p>
  </section>

  <section class="tile price bicycle">
    <svg width="200" height="120" viewBox="0 0 200 120" aria-hidden="true">
      <g fill="none" stroke="#111" stroke-width="9" stroke-linejoin="round" stroke-linecap="round">
        <circle cx="42" cy="80" r="33"/>
        <circle cx="158" cy="80" r="33"/>
        <polyline points="42,80 72,32 140,32 158,80"/>
        <polyline points="42,80 98,80 140,32"/>
        <line x1="72" y1="32" x2="98" y2="80"/>
        <line x1="62" y1="16" x2="84" y2="16"/>
        <line x1="72" y1="16" x2="72" y2="32"/>
        <polyline points="136,10 154,10 140,32"/>
      </g>
      <circle cx="98" cy="80" r="9" fill="#111"/>
    </svg>
    <p class="tile__label">$99.00/season + tax</p>
  </section>

  <section class="tile contact phone">
    <svg width="120" height="120" viewBox="0 0 120 120" aria-hidden="true">
      <path d="M60 8 A52 52 0 1 1 20 94" fill="none" stroke="#fff" stroke-width="8" stroke-linecap="round"/>
      <path d="M44 32 L54 44 L48 52 C52 62 60 70 68 74 L76 68 L88 78 L82 88 C60 90 32 62 34 40 Z" fill="#fff"/>
    </svg>
    <p class="tile__label">306-555-0148</p>
  </section>

  <section class="tile contact address">
    <svg width="80" height="120" viewBox="0 0 80 120" aria-hidden="true">
      <path d="M40 118 C30 92 4 66 4 40 A36 36 0 0 1 76 40 C76 66 50 92 40 118 Z" fill="#fff"/>
      <circle cx="40" cy="38" r="10" fill="var(--crimson)"/>
    </svg>
    <p class="tile__label">Vault 9 Nook Storage,<br>4718 Brindle Avenue, Saskatoon,<br>SK, S4M 2J6</p>
  </section>

  <section class="tile contact web">
    <svg width="120" height="120" viewBox="0 0 120 120" aria-hidden="true">
      <circle cx="60" cy="60" r="56" fill="#fff"/>
      <rect x="0" y="42" width="120" height="36" fill="var(--maroon)"/>
      <text x="60" y="72" text-anchor="middle" font-family="Arimo, Arial, sans-serif" font-weight="700" font-size="34" fill="#fff">WWW</text>
    </svg>
    <p class="tile__label">www.vault9nook.ca</p>
  </section>

</main>
</body>
</html>
```